Bright Fern Custom Homes business card. Double sided. Modern. professional

Bright Fern Custom Homes
contemporary modern design with our logo /
Double sided with all our contact information
Use same Green colors as in our Logo. Contemporary logo that grabs your attention. Visually pleasing and balanced. Easy to read, and Vibrant. Would love an option for rounded edges. Embossed logo would be amazing.
Contact Information for Business Card
Dana Welk Owner / General Contractor Bright Fern Custom Homes p: 704.552.1830 m: 912.648.2071 e: brightferncustomhomes@mailbox.example w: www.brightferncustomhomes.example 218 Pryor Meadow Lane Elmwick, SC 29041

```html
<!DOCTYPE html>
<html lang="en">
<head>
<meta charset="utf-8">
<title>Bright Fern Custom Homes – Business Card</title>
<link rel="stylesheet" href="https://fonts.googleapis.com/css2?family=Source+Serif+4:wght@400&display=swap">
<style>
  :root {
    --mint: #e8f8f4;
    --night: #030608;
    --fern: #5b6e30;
    --fern-light: #74893a;
    --white: #ffffff;
  }
  * { margin: 0; padding: 0; box-sizing: border-box; }
  html, body { width: 1019px; height: 1200px; overflow: hidden; background: var(--night); }
  body { font-family: "Source Serif 4", Georgia, serif; color: var(--fern); }

  .card-front {
    position: absolute; left: 0; top: 0; width: 1019px; height: 600px;
    background: var(--mint); overflow: hidden;
  }
  .front-accent {
    position: absolute; left: 590px; top: 170px; width: 560px; height: 560px;
    border-radius: 50%; background: var(--fern);
  }
  .person-name {
    position: absolute; left: 60px; top: 56px;
    font-size: 66px; line-height: 1; letter-spacing: 0.5px; font-weight: 400;
  }
  .person-role {
    position: absolute; left: 68px; top: 140px;
    font-size: 36px; line-height: 1; font-weight: 400;
  }
  .contact-icon {
    position: absolute; left: 50px; width: 50px; height: 50px;
  }
  .contact-text {
    position: absolute; left: 131px;
    font-size: 24px; line-height: 35px;
  }

  .card-back {
    position: absolute; left: 0; top: 600px; width: 1019px; height: 600px;
    background: var(--night);
  }
  .brand-dot {
    position: absolute; left: 444px; top: 160px; width: 130px; height: 130px;
    border-radius: 50%; background: var(--fern-light);
  }
  .brand-name {
    position: absolute; left: 0; width: 1019px; top: 382px; text-align: center;
    color: var(--fern); font-weight: 400; line-height: 1;
  }
  .brand-name .brand-main { display: block; font-size: 46px; letter-spacing: 10px; padding-left: 10px; }
  .brand-name .brand-sub { display: block; font-size: 14px; letter-spacing: 13px; padding-left: 13px; margin-top: 6px; }
  .brand-web {
    position: absolute; left: 0; width: 1019px; top: 476px; text-align: center;
    font-size: 24px; color: var(--fern);
  }
</style>
</head>
<body>
  <section class="card-front">
    <div class="front-accent" aria-hidden="true"></div>

    <h1 class="person-name">DANA WELK</h1>
    <p class="person-role">OWNER</p>

    <svg class="contact-icon" style="top:195px" viewBox="0 0 50 50" aria-hidden="true">
      <circle cx="25" cy="25" r="25" fill="var(--fern)"/>
      <path d="M25 11a9 9 0 0 0-9 9c0 7 9 16 9 16s9-9 9-16a9 9 0 0 0-9-9z" fill="var(--white)"/>
      <circle cx="25" cy="20" r="3.5" fill="var(--fern)"/>
      <ellipse cx="25" cy="38" rx="7" ry="1.6" fill="none" stroke="var(--white)" stroke-width="1.5"/>
    </svg>
    <p class="contact-text" style="top:199px">218 Pryor Meadow Lane<br>Elmwick, SC 29041</p>

    <svg class="contact-icon" style="top:273px" viewBox="0 0 50 50" aria-hidden="true">
      <circle cx="25" cy="25" r="25" fill="var(--fern)"/>
      <path d="M16 13c2-1 3 0 4 2l2 4c1 2 0 3-1 4l-1 1c1 3 4 6 7 7l1-1c1-1 2-2 4-1l4 2c2 1 3 2 2 4-1 3-4 4-7 3-7-2-13-8-15-15-1-3 0-6 0-10z" fill="var(--white)"/>
      <path d="M27 14a9 9 0 0 1 9 9M27 19a4 4 0 0 1 4 4" fill="none" stroke="var(--white)" stroke-width="1.6"/>
    </svg>
    <p class="contact-text" style="top:281px">704.552.1830</p>

    <svg class="contact-icon" style="top:343px" viewBox="0 0 50 50" aria-hidden="true">
      <circle cx="25" cy="25" r="25" fill="var(--fern)"/>
      <rect x="16" y="9" width="18" height="32" rx="3" fill="var(--white)"/>
      <rect x="18.5" y="13" width="13" height="21" fill="var(--fern)"/>
      <rect x="22" y="36.5" width="6" height="1.6" fill="var(--fern)"/>
    </svg>
    <p class="contact-text" style="top:349px">912.648.2071</p>

    <svg class="contact-icon" style="top:413px" viewBox="0 0 50 50" aria-hidden="true">
      <circle cx="25" cy="25" r="25" fill="var(--fern)"/>
      <rect x="11" y="16" width="28" height="18" fill="none" stroke="var(--white)" stroke-width="2"/>
      <path d="M11 16l14 11 14-11M11 34l10-9M39 34l-10-9" fill="none" stroke="var(--white)" stroke-width="2"/>
    </svg>
    <p class="contact-text" style="top:401px">brightferncustomhomes@mailbox<br>.example</p>

    <svg class="contact-icon" style="top:477px" viewBox="0 0 50 50" aria-hidden="true">
      <circle cx="25" cy="25" r="25" fill="var(--fern)"/>
      <g fill="none" stroke="var(--white)" stroke-width="1.6">
        <circle cx="25" cy="25" r="14"/>
        <ellipse cx="25" cy="25" rx="6" ry="14"/>
        <path d="M11 25h28M13 18h24M13 32h24M25 11v28"/>
      </g>
    </svg>
    <p class="contact-text" style="top:473px">www.brightferncustomhomes<br>.example</p>
  </section>

  <section class="card-back">
    <div class="brand-dot" aria-hidden="true"></div>
    <h2 class="brand-name">
      <span class="brand-main">BRIGHT FERN</span>
      <span class="brand-sub">CUSTOM HOMES</span>
    </h2>
    <p class="brand-web">www.brightferncustomhomes.example</p>
  </section>
</body>
</html>
```